Flyer Design for an ornamental (Aquarium) food product called Prawn Joy Quince

To design a product flyer for an ornamental (aquarium) food which is primarily made from the leaf of a Mulberry Tree. The flyer is a front and back however the back will be very simple, focus of the design is the first page of the PowerPoint.

• I have made a template in PowerPoint to base the design off of but please your creativity and design.

• Goals: Simple but eloquent

Target Market(s)

Home Aquarium Industry

Industry/Entity Type

Pet

Colors

Designer to choose colors to be used in the design.

Requirements
Must have
• • In the PowerPoint I have used a photo of a real shrimp over heart but I would like the design to use a created graphic of a shrimp (please look up “crystal red shrimp” – and there are even graphic versions of ornamental shrimp to use as reference when image searched). Please do NOT use image/graphic of a shrimp that is used for human consumption.
• The name of the product is "Prawn Joy Quince", on the design please use a graphic of a heart to represent the word "Love" - similar to the PowerPoint.
Nice to have
• • Colour: Open to creative design in you can convince me, but I do like white background, red for the heart, dark green relates to the mulberry leaves.
• • Font – You do not need to use the font in the PowerPoint, use whatever font you think looks best
Should not have
• Please do NOT use image/graphic of a shrimp that is used for human consumption.
• As described in the must haves: (please look up “crystal red shrimp” – and there are even graphic versions of ornamental shrimp to use as reference when image searched)."

```html
<!DOCTYPE html>
<html lang="en">
<head>
<meta charset="utf-8">
<title>Prawn Joy Quince – Flyer Front and Back</title>
<link href="https://fonts.googleapis.com/css2?family=Montserrat:wght@800;900&family=Roboto:wght@400;500;700&display=swap" rel="stylesheet">
<style>
  :root {
    --backdrop: #e9e6e1;
    --paper: #f5f2ec;
    --paper-edge: #e8e0d2;
    --ink: #1d1d1d;
    --red: #e3101c;
    --heart-red: #d9101c;
    --shrimp: #f07f6c;
    --leaf: #4f8a3a;
    --berry: #5a1f3a;
  }
  * { box-sizing: border-box; margin: 0; padding: 0; }
  html, body { width: 1200px; height: 1200px; overflow: hidden; }
  body {
    background: var(--backdrop);
    font-family: "Roboto", Arial, sans-serif;
    color: var(--ink);
    position: relative;
  }
  .page {
    position: absolute;
    top: 227px;
    width: 530px;
    height: 745px;
    background: radial-gradient(ellipse at center, var(--paper) 55%, var(--paper-edge) 100%);
    box-shadow: 0 6px 18px rgba(0,0,0,.18);
  }
  .page--front { left: 50px; }
  .page--back { left: 620px; }
  .frame {
    position: absolute;
    left: 22px; right: 22px; top: 14px; bottom: 12px;
    border: 1.5px solid var(--ink);
    border-radius: 14px;
  }
  .leaf-corner {
    position: absolute; top: 0;
    width: 70px; height: 70px;
    background: radial-gradient(circle at var(--cx) 0, var(--leaf) 0 38%, rgba(79,138,58,.35) 55%, transparent 72%);
  }
  .leaf-corner--left { left: 0; --cx: 0; }
  .leaf-corner--right { right: 0; --cx: 100%; }
  .artwork {
    position: absolute;
    border-radius: 50% 50% 46% 46%;
    background: radial-gradient(circle at 55% 60%, var(--shrimp) 0 22%, rgba(217,16,28,.75) 38%, rgba(217,16,28,.15) 62%, transparent 72%);
  }
  .page--front .artwork { left: 120px; top: 16px; width: 345px; height: 330px; }
  .page--back .artwork { left: 18px; top: 18px; width: 220px; height: 215px; }

  .title {
    position: absolute; left: 0; right: 0;
    text-align: center;
    font-family: "Montserrat", Arial, sans-serif;
    font-weight: 900;
    line-height: 1;
  }
  .title--top { top: 336px; font-size: 44px; color: var(--red); }
  .title--bottom { top: 392px; font-size: 47px; color: var(--ink); letter-spacing: .5px; }
  .subheading {
    position: absolute; left: 0; right: 0; top: 472px;
    text-align: center;
  }
  .subheading span {
    display: inline-block;
    font-weight: 500; font-size: 15.5px;
    padding: 0 2px 3px;
    border-bottom: 1.2px solid var(--ink);
  }
  .benefits {
    position: absolute; left: 0; right: 0; top: 531px;
    list-style: none; text-align: center;
    font-weight: 500; font-size: 11.5px;
  }
  .benefits li { height: 21.6px; }

  .web-line {
    position: absolute; left: 0; right: 0; top: 690px;
    height: 1.2px; background: var(--red);
  }
  .web-address {
    position: absolute; left: 0; right: 0; top: 682px;
    text-align: center;
  }
  .web-address span {
    display: inline-block;
    background: var(--paper);
    padding: 0 10px;
    font-weight: 700; font-size: 11.5px; letter-spacing: 2.6px;
    position: relative;
  }
  .web-address span::before, .web-address span::after {
    content: ""; position: absolute; top: 5px;
    width: 6px; height: 6px; border-radius: 50%; background: var(--red);
  }
  .web-address span::before { left: -3px; }
  .web-address span::after { right: -3px; }
  .net-weight {
    position: absolute; left: 0; right: 0; top: 710px;
    text-align: center; font-size: 11px; font-weight: 500; color: var(--red);
  }

  .intro {
    position: absolute; left: 255px; width: 240px; top: 131px;
    font-size: 10px; line-height: 1.25; text-align: justify;
  }
  .info {
    position: absolute; left: 45px; width: 455px;
    font-size: 10px; line-height: 1.25;
  }
  .info h2 { font-size: 11.5px; font-weight: 700; color: var(--red); margin-bottom: 6px; }
  .info--feeding { top: 298px; }
  .info--storage { top: 370px; }
  .pin { position: absolute; left: 250px; top: 478px; }
  .producer {
    position: absolute; left: 0; right: 0; top: 536px;
    text-align: center; font-size: 10.5px; line-height: 1.2;
  }
</style>
</head>
<body>

<section class="page page--front">
  <div class="leaf-corner leaf-corner--left" role="img" aria-label="Mulberry leaves and berries corner decoration"></div>
  <div class="leaf-corner leaf-corner--right" role="img" aria-label="Mulberry leaves and berries corner decoration"></div>
  <div class="frame"></div>
  <div class="artwork" role="img" aria-label="Red brush-stroke heart with an illustrated crystal red shrimp"></div>
  <h1 class="title title--top">PRAWN</h1>
  <p class="title title--bottom">QUINCE</p>
  <div class="subheading"><span>MULBERRY LEAVES ARE A NATURAL SOURCE OF</span></div>
  <ul class="benefits">
    <li>Vitamin A, B, C, and K</li>
    <li>Calcium, Iron, &amp; Potassium</li>
    <li>Dietary Fibre</li>
    <li>Beneficial phytonutrients</li>
    <li>Best of all shrimp LOVE it!!!</li>
  </ul>
  <div class="web-line"></div>
  <div class="web-address"><span>www.prawnjoyquince.com</span></div>
  <p class="net-weight">Net Weight: Four x 3g tubes</p>
</section>

<section class="page page--back">
  <div class="leaf-corner leaf-corner--left" role="img" aria-label="Mulberry leaves and berries corner decoration"></div>
  <div class="leaf-corner leaf-corner--right" role="img" aria-label="Mulberry leaves and berries corner decoration"></div>
  <div class="frame"></div>
  <div class="artwork" role="img" aria-label="Red brush-stroke heart with an illustrated crystal red shrimp"></div>
  <p class="intro">Prawn Joy Quince is designed to be used as part of a varied diet for your shrimp. It comes in a convenient applicator to easily control and provide the exact amount of food you want to feed.</p>
  <div class="info info--feeding">
    <h2>Feeding Instructions:</h2>
    <p>Use as part of a varied diet for your shrimp. Feed once a day, the amount will vary with the number of shrimp present.&nbsp; Avoid over feeding and remove any uneaten food to avoid water quality issues.</p>
  </div>
  <div class="info info--storage">
    <h2>Storage:</h2>
    <p>Keep frozen for long term storage. Remove one applicator at time.&nbsp; After an applicator is removed from the freezer and thawed discard any remaining food after one month.&nbsp; Store the applicator in the refrigerator between feedings.</p>
  </div>
  <svg class="pin" width="30" height="34" viewBox="0 0 30 34" aria-hidden="true">
    <path d="M15 2a7 7 0 0 0-7 7c0 5 7 13 7 13s7-8 7-13a7 7 0 0 0-7-7z" fill="#e3101c"/>
    <circle cx="15" cy="9" r="2.6" fill="#f5f2ec"/>
    <path d="M9 22H4L2 32h26l-2-10h-5" fill="none" stroke="#e3101c" stroke-width="2"/>
  </svg>
  <p class="producer">Produced in Australia by:<br>Prawn Joy Quince<br>PO Box 2045<br>Kingsford West, VIC 3182</p>
  <div class="web-line"></div>
  <div class="web-address"><span>www.prawnjoyquince.com</span></div>
</section>

</body>
</html>
```